Golf Tournament Flyer and Header Needed

Non-profit needs a flyer for their benefit golf tournament - "Wild Socks Charity Golf Classic"

Target Market(s)

Design and Construction industry professionals

Industry/Entity Type

Design and Construction

Colors

Designer to choose colors to be used in the design.

Requirements
Must have
• Date: September 22, 2021, 8:00 AM Shotgun Start, Location: Marrowind Links Club. Q-BevTR Logo
Nice to have
• Would like image of golfers in Wild Socks incorporated.

```html
<!DOCTYPE html>
<html lang="en">
<head>
<meta charset="utf-8">
<title>Wild Socks Invitational Golf Tournament – Headers</title>
<link rel="stylesheet" href="https://fonts.googleapis.com/css2?family=Montserrat:wght@800;900&family=Oswald:wght@500&family=Poppins:wght@500&family=Raleway:wght@400;700&display=swap">
<style>
  :root {
    --stage: #939598;
    --slate: #58585a;
    --royal: #36509f;
    --lime: #8db33e;
    --white: #ffffff;
    --sky: #9cc3e6;
    --turf: #6f9a3c;
  }
  html, body {
    margin: 0;
    padding: 0;
    width: 972px;
    height: 1200px;
    overflow: hidden;
    background: var(--stage);
  }
  .sheet {
    position: relative;
    width: 972px;
    height: 1200px;
  }
  .banner {
    position: absolute;
    left: 64px;
    width: 843px;
    height: 297px;
    display: block;
  }
  .banner--slate-left { top: 67px; }
  .banner--slate-right { top: 454px; }
  .banner--royal-right { top: 836px; }

  .fill-slate { fill: var(--slate); }
  .fill-royal { fill: var(--royal); }
  .fill-lime { fill: var(--lime); }
  .fill-white { fill: var(--white); }
  .rule-lime { stroke: var(--lime); stroke-width: 5; }
  .rule-white { stroke: var(--white); stroke-width: 3; }

  .event-name { font-family: "Raleway", sans-serif; font-weight: 700; fill: var(--white); }
  .event-name--lime { fill: var(--lime); }
  .event-kind { font-family: "Raleway", sans-serif; font-weight: 400; fill: var(--white); }
  .event-kind--condensed { font-family: "Oswald", sans-serif; font-weight: 500; fill: var(--lime); }
  .sport { font-family: "Montserrat", sans-serif; font-weight: 900; fill: var(--white); }
  .format { font-family: "Raleway", sans-serif; font-weight: 400; fill: var(--white); }
  .detail-label { font-family: "Poppins", sans-serif; font-weight: 500; fill: var(--lime); font-size: 20px; }
  .detail-value { font-family: "Poppins", sans-serif; font-weight: 500; fill: var(--white); font-size: 20px; }
  .org-name { font-family: "Poppins", sans-serif; font-weight: 500; fill: var(--slate); }
  .org-tagline { font-family: "Poppins", sans-serif; font-weight: 500; fill: var(--lime); }
</style>
</head>
<body>
<main class="sheet">

  <!-- Header A: slate field left, team photo right -->
  <svg class="banner banner--slate-left" viewBox="0 0 1505 530" xmlns="http://www.w3.org/2000/svg">
    <defs>
      <linearGradient id="teamTonesA" x1="0" y1="0" x2="0" y2="1">
        <stop offset="0" stop-color="var(--sky)"/>
        <stop offset="0.45" stop-color="#c9d9e2"/>
        <stop offset="0.6" stop-color="var(--turf)"/>
        <stop offset="1" stop-color="#5e8a30"/>
      </linearGradient>
    </defs>
    <rect class="fill-slate" width="1505" height="530"/>
    <polygon class="fill-royal" points="342,0 702,0 874,322 762,530 620,530"/>
    <polygon fill="url(#teamTonesA)" points="1042,0 1505,0 1505,530 1060,530 912,251"
             role="img" aria-label="Photo of four golfers in white polos and blue argyle trousers on a course"/>
    <polygon class="fill-lime" points="702,0 1042,0 872,318"/>
    <polygon class="fill-white" points="912,251 1060,530 762,530"/>

    <text class="event-name" x="157" y="94" font-size="58" textLength="393" lengthAdjust="spacingAndGlyphs">WILD SOCKS</text>
    <line class="rule-white" x1="157" y1="131" x2="205" y2="131"/>
    <text class="event-kind" x="356" y="149" font-size="50" text-anchor="middle">Invitational</text>
    <line class="rule-white" x1="502" y1="131" x2="550" y2="131"/>

    <line class="rule-lime" x1="130" y1="247" x2="213" y2="247"/>
    <text class="sport" x="350" y="276" font-size="86" text-anchor="middle">GOLF</text>
    <line class="rule-lime" x1="486" y1="247" x2="569" y2="247"/>
    <text class="format" x="130" y="330" font-size="50" textLength="440" lengthAdjust="spacing">TOURNAMENT</text>

    <text class="detail-label" x="135" y="389">Date:</text>
    <text class="detail-value" x="135" y="418">September 22, 2021</text>
    <text class="detail-value" x="135" y="446">8:00 AM</text>
    <text class="detail-value" x="135" y="474">Shotgun Start</text>
    <line class="rule-lime" x1="367" y1="374" x2="367" y2="474" style="stroke-width:3"/>
    <text class="detail-label" x="400" y="389">Location:</text>
    <text class="detail-value" x="400" y="418">Marrowind Links Club</text>

    <circle class="fill-royal" cx="910" cy="389" r="38"/>
    <text class="org-name" x="910" y="471" font-size="40" text-anchor="middle">Q-BevTR</text>
    <text class="org-tagline" x="910" y="492" font-size="9" text-anchor="middle">Quorum for Better Venue and Trade Relations</text>
  </svg>

  <!-- Header B: team photo left, slate field right -->
  <svg class="banner banner--slate-right" viewBox="0 0 1505 530" xmlns="http://www.w3.org/2000/svg">
    <defs>
      <linearGradient id="teamTonesB" x1="0" y1="0" x2="0" y2="1">
        <stop offset="0" stop-color="var(--sky)"/>
        <stop offset="0.45" stop-color="#c9d9e2"/>
        <stop offset="0.6" stop-color="var(--turf)"/>
        <stop offset="1" stop-color="#5e8a30"/>
      </linearGradient>
    </defs>
    <rect class="fill-slate" width="1505" height="530"/>
    <polygon fill="url(#teamTonesB)" points="0,0 447,0 582,251 433,530 0,530"
             role="img" aria-label="Photo of four golfers in white polos and blue argyle trousers on a course"/>
    <polygon class="fill-royal" points="447,0 805,0 948,249 817,530 735,530 582,251"/>
    <polygon class="fill-lime" points="805,0 1077,0 948,249"/>
    <polygon class="fill-white" points="582,251 735,530 433,530"/>

    <text class="event-name" x="840" y="104" font-size="88" text-anchor="end">WILD</text>
    <text class="event-name" x="882" y="194" font-size="88" text-anchor="end">SOCKS</text>
    <text class="event-kind" x="917" y="259" font-size="60" text-anchor="end">Invitational</text>

    <line class="rule-lime" x1="988" y1="177" x2="1070" y2="177"/>
    <text class="sport" x="1208" y="202" font-size="86" text-anchor="middle">GOLF</text>
    <line class="rule-lime" x1="1345" y1="177" x2="1427" y2="177"/>
    <text class="format" x="988" y="259" font-size="52" textLength="440" lengthAdjust="spacing">TOURNAMENT</text>

    <text class="detail-label" x="988" y="362">Date:</text>
    <text class="detail-value" x="988" y="391">September 22, 2021</text>
    <text class="detail-value" x="988" y="419">8:00 AM</text>
    <text class="detail-value" x="988" y="447">Shotgun Start</text>
    <line class="rule-lime" x1="1221" y1="347" x2="1221" y2="446" style="stroke-width:3"/>
    <text class="detail-label" x="1253" y="362">Location:</text>
    <text class="detail-value" x="1253" y="391">Marrowind Links Club</text>

    <circle class="fill-royal" cx="582" cy="389" r="38"/>
    <text class="org-name" x="582" y="471" font-size="40" text-anchor="middle">Q-BevTR</text>
    <text class="org-tagline" x="582" y="492" font-size="9" text-anchor="middle">Quorum for Better Venue and Trade Relations</text>
  </svg>

  <!-- Header C: team photo left, white diagonal, royal field right -->
  <svg class="banner banner--royal-right" viewBox="0 0 1505 530" xmlns="http://www.w3.org/2000/svg">
    <defs>
      <linearGradient id="teamTonesC" x1="0" y1="0" x2="0" y2="1">
        <stop offset="0" stop-color="var(--sky)"/>
        <stop offset="0.45" stop-color="#c9d9e2"/>
        <stop offset="0.6" stop-color="var(--turf)"/>
        <stop offset="1" stop-color="#5e8a30"/>
      </linearGradient>
    </defs>
    <rect class="fill-white" width="1505" height="530"/>
    <polygon fill="url(#teamTonesC)" points="0,0 437,0 592,264 433,530 0,530"
             role="img" aria-label="Photo of four golfers in white polos and blue argyle trousers on a course"/>
    <polygon class="fill-lime" points="437,0 745,0 592,264"/>
    <polygon class="fill-royal" points="1032,0 1505,0 1505,295 1379,530 737,530"/>

    <text class="event-name event-name--lime" x="732" y="97" font-size="58" textLength="200" lengthAdjust="spacingAndGlyphs">WILD</text>
    <text class="event-name event-name--lime" x="732" y="155" font-size="58" textLength="200" lengthAdjust="spacingAndGlyphs">SOCKS</text>
    <text class="event-kind event-kind--condensed" x="945" y="155" font-size="120" textLength="477" lengthAdjust="spacingAndGlyphs">Invitational</text>

    <line class="rule-lime" x1="918" y1="260" x2="1002" y2="260"/>
    <text class="sport" x="1138" y="287" font-size="86" text-anchor="middle">GOLF</text>
    <line class="rule-lime" x1="1275" y1="260" x2="1358" y2="260"/>
    <text class="format" x="918" y="342" font-size="52" textLength="442" lengthAdjust="spacing">TOURNAMENT</text>

    <text class="detail-label" x="918" y="400">Date:</text>
    <text class="detail-value" x="918" y="428">September 22, 2021</text>
    <text class="detail-value" x="918" y="456">8:00 AM</text>
    <text class="detail-value" x="918" y="484">Shotgun Start</text>
    <line class="rule-lime" x1="1152" y1="385" x2="1152" y2="484" style="stroke-width:3"/>
    <text class="detail-label" x="1185" y="400">Location:</text>
    <text class="detail-value" x="1185" y="428">Marrowind Links Club</text>

    <circle class="fill-royal" cx="618" cy="360" r="48"/>
    <text class="org-name" x="618" y="462" font-size="52" text-anchor="middle">Q-BevTR</text>
    <text class="org-tagline" x="618" y="492" font-size="11" text-anchor="middle">Quorum for Better Venue and Trade Relations</text>
  </svg>

</main>
</body>
</html>
```